Startup Drone Platform Company business card

We are needing a business card design for our employees. We are a startup drone platform. We are looking for a business card that has our logo on one side, with the employee/company details on the opposite side. We are looking for something that is very eye catching, modern, and bold.

Target Market(s)

This will target both drone pilots and drone businesses, along with all the industries that could utilize drone services (aerial video, aerial photos, inspections, 3d mapping, etc).

Industry/Entity Type

Business

```html
<!DOCTYPE html>
<html lang="en">
<head>
<meta charset="utf-8">
<title>Skyvane Aerial – Business Card</title>
<link href="https://fonts.googleapis.com/css2?family=Source+Sans+3:wght@400;600&display=swap" rel="stylesheet">
<style>
  :root {
    --stage-top: #2c2c2c;
    --stage-bottom: #050505;
    --card-light: #f3f3f3;
    --card-teal: #3bbac6;
    --ink: #1d1d1d;
    --accent: #1aa8d6;
    --white: #ffffff;
  }
  * { margin: 0; padding: 0; box-sizing: border-box; }
  html, body { width: 1200px; height: 900px; overflow: hidden; }
  body {
    position: relative;
    background: linear-gradient(180deg, var(--stage-top) 0%, #161616 60%, var(--stage-bottom) 100%);
    font-family: "Source Sans 3", "Myriad Pro", Arial, sans-serif;
  }
  .card {
    position: absolute;
    top: 184px;
    height: 490px;
    border-radius: 14px;
    box-shadow: 0 6px 18px rgba(0,0,0,0.45);
    text-align: center;
  }
  .card--details { left: 299px; width: 301px; background: var(--card-light); color: var(--ink); }
  .card--brand { left: 645px; width: 304px; background: var(--card-teal); color: var(--white); }

  .brand-mark { position: absolute; left: 0; right: 0; }
  .brand-mark__dot {
    display: block; margin: 0 auto;
    width: 70px; height: 70px; border-radius: 50%;
    border: 3px solid var(--card-teal);
  }
  .brand-mark__name {
    font-weight: 400; letter-spacing: 0.32em; line-height: 1;
    padding-left: 0.32em;
  }
  .card--details .brand-mark { top: 62px; }
  .card--details .brand-mark__name--main { font-size: 20px; margin-top: 58px; }
  .card--details .brand-mark__name--sub { font-size: 14px; margin-top: 8px; }

  .card--brand .brand-mark { top: 380px; }
  .card--brand .brand-mark__name--main { font-size: 32px; letter-spacing: 0.3em; }
  .card--brand .brand-mark__name--sub { font-size: 21px; margin-top: 16px; letter-spacing: 0.3em; }

  .person { position: absolute; top: 284px; left: 0; right: 0; padding-left: 6px; }
  .person__name { font-size: 17px; font-weight: 600; color: var(--accent); line-height: 1.2; }
  .person__role { font-size: 14px; margin-top: 2px; padding-left: 8px; }

  .contact { position: absolute; top: 354px; left: 0; right: 0; font-size: 13.5px; line-height: 17px; }
  .address { position: absolute; top: 427px; left: 0; right: 0; font-size: 13.5px; line-height: 16px; }
</style>
</head>
<body>
  <section class="card card--details" aria-label="Business card, contact side">
    <div class="brand-mark">
      <span class="brand-mark__dot" aria-hidden="true"></span>
      <p class="brand-mark__name brand-mark__name--main">SKYVANE</p>
      <p class="brand-mark__name brand-mark__name--sub">AERIAL</p>
    </div>
    <div class="person">
      <p class="person__name">DANIEL ARCHER</p>
      <p class="person__role">Managing Director</p>
    </div>
    <div class="contact">
      <p>044-555-0182</p>
      <p>hello@skyvaneaerial.com</p>
      <p>www.skyvaneaerial.com</p>
    </div>
    <div class="address">
      <p>88 Hangar Row |</p>
      <p>Northfield, AB | 204519</p>
    </div>
  </section>

  <section class="card card--brand" aria-label="Business card, brand side">
    <div class="brand-mark">
      <p class="brand-mark__name brand-mark__name--main">SKYVANE</p>
      <p class="brand-mark__name brand-mark__name--sub">AERIAL</p>
    </div>
  </section>
</body>
</html>
```